Secret agents need a new website

We organize child birthdays with a special agents in london & Bristol.

Current design does not grab people attention, and they leave website too soon.

Colors. Up to 3 main colors, but maybe black + green + white, or blact + red + white, would suit our secret operations website.

Current website:
www.moonjumble.co.uk

Dear designers, thanks very much for working on our design.

Please try to make like a SPECIAL YOUNG AGENT TRAINING WEBSITE, all other
entertainers have childish websites, and we want to differentiate from them.

Not sure if it helps, but I like this design very much:

Guys,

I am looking for spy/secret agent/action themed design. You submitting awesome designs, and if I have another business, I just choose any of them at it would be perfect. But I want spy/secret agent/action themed.

Please feel free to add elements like:

1. Yellow, or RED line CRIME SCENE DO NOT CROSS
2. Some words or phrases can be black background - white text. 
3. Some stamps like this:
http://www.plenvoria.com/pic-48120957/stock-vector-assorted-office-ink-marks-classified-private-etc.html?src=qTm4Lo-bRwNxZ3e-p81KcE-1-16

4.spy guys http://www.plenvoria.com/pic-39418275/stock-vector-sleuth-in-long-overcoat-vintage-clip-art.html?src=hdWpRmTeQoXs4v9bnaLjCf-1-9

Do not make too much elements, I like simple designs, less details.  

PLEASE NO CHILDS WITH GUNS, and better NO GUNS at all. 

Target Market(s)

Audience: Woman, but should look cool for kids too.
(Please DO NOT make design childish)

Requirements
Must have
• Please take a look at current website
• 1. Texts should be easy to read and not too small.
• 2. White/bright background
• 3. Lead form should stay on page
• 4. Header, and footer should be not too big.
• 5. Infographic is not needed
• Extra elements
• 1. Company blog
• 2. Client zone
• 3. Venue finder
• 4. How to pay deposit
Nice to have
• We accept
• Quidlo
• marrowfeld
• (please browse logos)
• On header would be better to use
• MoonJumble.co.uk
• But also add somethere, in association with Fen-rally.co.uk.
• Please use logo with .co.uk
• In archive you will find without background if needed too.

```html
<!DOCTYPE html>
<html lang="en">
<head>
<meta charset="utf-8">
<title>Blog – Fen-rally.co.uk</title>
<link rel="stylesheet" href="https://fonts.googleapis.com/css2?family=Londrina+Solid:wght@400;900&family=Roboto:ital,wght@0,400;0,500;1,400&display=swap">
<style>
:root{
  --red:#c8161d;
  --red-dark:#a10f14;
  --green:#52a82a;
  --ink:#222;
  --text:#555;
  --muted:#999;
  --line:#e3e3e3;
  --paper:#fff;
  --concrete:#d9d9d9;
  --footer:#1e1e1e;
}
*{box-sizing:border-box;margin:0;padding:0}
html,body{width:1187px;height:1200px;overflow:hidden}
body{position:relative;font-family:"Roboto",Arial,sans-serif;color:var(--text);background:var(--concrete)}
.backdrop{position:absolute;inset:0 0 123px 0;background:radial-gradient(ellipse at 50% 30%,#eeeeee 0%,#d6d6d6 60%,#c4c4c4 100%)}
.abs{position:absolute}
.brand{left:88px;top:42px;font-family:"Londrina Solid",sans-serif;font-weight:900;font-size:38px;color:var(--green);display:flex;align-items:center;gap:10px}
.brand .mark{width:26px;height:26px;background:var(--green)}
.follow{left:884px;top:22px;display:flex;align-items:center;gap:10px;font-family:"Londrina Solid",sans-serif;font-weight:900;font-size:17px;color:var(--ink);letter-spacing:1px}
.social{width:32px;height:32px;border-radius:5px;display:inline-block}
.social.s1{background:#3b5998}.social.s2{background:#3cc6ee}.social.s3{background:#d8221e}
.enquire{left:873px;top:67px;width:227px;height:50px;background:linear-gradient(#6cc43a,#3f9a1f);border:1px solid #2f7d14;border-radius:3px;color:#fff;font-family:"Londrina Solid",sans-serif;font-weight:900;font-size:30px;letter-spacing:2px;display:flex;align-items:center;justify-content:center}
.panel{left:87px;top:127px;width:1013px;height:950px;background:var(--paper);box-shadow:0 0 6px rgba(0,0,0,.25)}
.nav{left:75px;top:139px;width:1038px;height:47px;background:linear-gradient(var(--red),var(--red-dark));display:flex;justify-content:space-between;align-items:center;padding:0 14px 0 26px}
.nav a{color:#fff;text-decoration:none;font-family:"Londrina Solid",sans-serif;font-weight:900;font-size:26px;letter-spacing:1.5px}
.page-title{left:99px;top:214px;font-family:"Londrina Solid",sans-serif;font-weight:900;font-size:26px;color:var(--ink);letter-spacing:1px}
.crumbs{left:99px;top:257px;font-size:12px;color:var(--ink)}
.crumbs span{color:var(--red)}
.rule{left:99px;top:282px;width:950px;height:1px;background:var(--line)}
.post-title{left:100px;top:302px;font-size:23px;color:var(--red);letter-spacing:.3px}
.meta{left:100px;top:343px;font-size:12px;font-style:italic;color:var(--ink);display:flex;gap:16px;align-items:center}
.meta i{display:inline-block;width:14px;height:13px;background:#777;margin-right:6px;vertical-align:-2px;border-radius:2px}
.photo-frame{left:99px;top:379px;width:625px;height:243px;border:1px solid #ddd;padding:4px}
.photo{width:100%;height:100%;background:linear-gradient(135deg,#3e6b2a,#2a4a1c 55%,#4a3a30)}
.body-copy{left:100px;top:636px;width:625px;font-size:13px;line-height:23px}
.body-copy p{margin-bottom:8px}
.post-foot{left:99px;top:915px;width:625px;height:41px;border-top:1px solid var(--line);border-bottom:1px solid var(--line)}
.read-more{left:99px;top:921px;width:98px;height:30px;background:#333;color:#fff;font-size:12px;border-radius:2px;display:flex;align-items:center;justify-content:center}
.stats{left:485px;top:930px;font-size:11px;font-style:italic;color:var(--red);display:flex;gap:14px;align-items:center}
.stats b{display:inline-block;width:14px;height:10px;background:#999;margin-right:6px;border-radius:3px;vertical-align:-1px}
.back{left:100px;top:1019px;display:flex;align-items:center;gap:10px;font-size:14px;color:var(--red)}
.pager{left:549px;top:1014px;display:flex;border:1px solid #ddd;height:36px;font-size:13px}
.pager span{display:flex;align-items:center;justify-content:center;padding:0 13px;border-left:1px solid #ddd;color:#666}
.pager .on{background:var(--red);color:#fff;border:0;width:38px}
.pager .alt{background:#666;color:#fff;width:35px}
.side{left:772px;width:307px}
.side h3{font-weight:400;font-size:22px;color:#444;margin-bottom:12px;letter-spacing:.5px}
.side ul{list-style:none}
.side li{font-size:13px;color:var(--ink);height:32px;line-height:30px;border-bottom:1px solid var(--line);padding-left:23px;position:relative}
.side li:last-child{border-bottom:0}
.side li::before{content:"";position:absolute;left:1px;top:11px;width:8px;height:8px;border-radius:50%;background:var(--red)}
.footer{left:0;top:1077px;width:1187px;height:123px;background:var(--footer)}
.foot-links{left:107px;top:1101px;font-size:15px;color:#ddd}
.foot-links span{margin:0 9px;color:#aaa}
.copy{left:107px;top:1141px;font-size:12px;line-height:19px;color:#999}
.agent{left:720px;top:1077px;width:120px;height:123px;background:linear-gradient(#6a6a6a,#3a3a3a)}
.call-label{left:841px;top:1112px;font-family:"Londrina Solid",sans-serif;font-weight:900;font-size:18px;color:#eee;letter-spacing:1.5px}
.call-num{left:841px;top:1131px;font-family:"Londrina Solid",sans-serif;font-weight:900;font-size:36px;color:#e02a2a;letter-spacing:2px}
</style>
</head>
<body>
<div class="backdrop" role="img" aria-label="Grey concrete texture with crime scene tape and top secret stamps"></div>

<div class="abs brand"><span class="mark"></span>Fen-rally.co.uk</div>
<div class="abs follow">FOLLOW US:
  <span class="social s1" role="img" aria-label="Social network link"></span>
  <span class="social s2" role="img" aria-label="Social network link"></span>
  <span class="social s3" role="img" aria-label="Video channel link"></span>
</div>
<div class="abs enquire">ENQUIRE NOW</div>

<div class="abs panel"></div>
<nav class="abs nav">
  <a>HOME</a><a>EQUIPMENT INVITATIONS</a><a>PARTY BAGS</a><a>PRICES</a><a>BLOG</a><a>CONTACT</a>
</nav>

<h1 class="abs page-title">BLOG</h1>
<div class="abs crumbs">HOME &nbsp;|&nbsp; <span>BLOG</span></div>
<div class="abs rule"></div>

<h2 class="abs post-title">SED UT PERSPICIATIS UNDE</h2>
<div class="abs meta"><span><i></i>March 14, 2013</span><span><i></i>Admin</span></div>
<div class="abs photo-frame"><div class="photo" role="img" aria-label="Photo of five young agents in sunglasses posing in a garden"></div></div>
<div class="abs body-copy">
  <p>Lorem ipsum dolor sit amet, consectetur adipiscing elit. Sed blandit massa vel mauris sollicitudin dignissim. Phasellus ultrices tellus eget ipsum ornare molestie scelerisque eros dignissim. Phasellus fringilla hendrerit lectus nec vehicula. Pellentesque habitant morbi tristique senectus et netus et malesuada fames ac turpis egestas. In faucibus, risus eu volutpat pellentesque, massa felis feugiat velit, nec...</p>
  <p>Aliquam molestie, mi et imperdiet euismod, dui purus auctor tellus, et interdum lacus lectus et ante. Sed accumsan sollicitudin sapien, sit amet adipiscing turpis gravida ac. In congue, neque ac lobortis volutpat, libero mauris varius mi, vitae suscipit ipsum ligula vitae risus. Duis aliquam nibh a dui iaculis viverra id a velit. Vivamus egestas risus in magna varius commodo. Sed semper viverra egestas. Etiam pretium porttitor lectus, vel ornare neque porta volutpat.</p>
</div>
<div class="abs post-foot"></div>
<div class="abs read-more">READ MORE</div>
<div class="abs stats"><span><b></b>5 Comments</span><span><b></b>73</span><span><b></b>0</span><span><b></b>0</span></div>

<div class="abs back">
  <svg width="20" height="20" viewBox="0 0 20 20"><path d="M10 2 1 10h3v8h4v-5h4v5h4v-8h3z" fill="#777"/></svg>
  Back to Homepage
</div>
<div class="abs pager"><span class="on">1</span><span class="alt">2</span><span>Next</span><span>Last</span></div>

<aside class="abs side" style="top:298px">
  <h3>CATEGORIES</h3>
  <ul>
    <li>Aenean nec eros vestibulum ante ipsu</li>
    <li>Etiam cursus leo vel metus nulla facilisi</li>
    <li>Faucibus orci luctus et ultrices posuere</li>
    <li>Hendrerit sit amet tincidunt ac viverra se</li>
    <li>Suspendisse sollicitudin velit sed leo</li>
    <li>Uncategorized</li>
  </ul>
</aside>
<aside class="abs side" style="top:553px">
  <h3>ARCHIVES</h3>
  <ul>
    <li>March 2013</li><li>February 2013</li><li>January 2013</li><li>December 2012</li><li>May 2012</li>
  </ul>
</aside>

<footer class="abs footer"></footer>
<div class="abs foot-links">Contact us<span>|</span>About us<span>|</span>Terms and Conditions</div>
<div class="abs copy">Copyright © 2011-2013 Starlane Events Ltd.<br>All Right Reserved</div>
<div class="abs agent" role="img" aria-label="Illustration of a detective in hat and trench coat"></div>
<div class="abs call-label">GIVE US A CALL:</div>
<div class="abs call-num">020 3945 7718</div>
</body>
</html>
```